We are a Machine Engineering Company based in Singapore since 1978. We supply tools & machine accessories to Manufacturing Plants using CNC Machines.

We sell Drills / Taps / Reamers / Carbide & Ceramic Inserts / Arbors / Chucks / Vise / etc...

We need an E Christmas Card to send out to our customers Worldwide.
It should have our Company Logo.
It should also include Greetings for the New Year.

Target Market(s)

Manufacturers of Aero Space / Oil & Gas / Automotive / Medical Science / etc

Requirements
Must have
• Company Logo
• Link : www.tovalix.com.sg
Nice to have
• Modern Designs
Should not have
• Porn or Suggestive Pictures.

```html
<!DOCTYPE html>
<html lang="en">
<head>
<meta charset="utf-8">
<title>Tovalix Tools – Season's Greetings 2015</title>
<link rel="stylesheet" href="https://fonts.googleapis.com/css2?family=Righteous&family=Roboto:wght@400;700&display=swap">
<style>
  :root {
    --bg-purple: #5e2a86;
    --bg-magenta: #a8185a;
    --bg-crimson: #c3163f;
    --bg-red: #d3222c;
    --headline-pink: #f25fd6;
    --headline-rose: #ff6c9c;
    --year-pink: #ff3d9a;
    --body-pink: #ff2f8f;
    --card-white: #f3f3f3;
    --brand-red: #9c1a3c;
    --ink: #1a1a1a;
  }
  * { margin: 0; padding: 0; box-sizing: border-box; }
  html, body { width: 1200px; height: 900px; overflow: hidden; background: #ffffff; }
  .greeting-card {
    position: relative;
    width: 1200px;
    height: 900px;
    overflow: hidden;
  }
  .backdrop {
    position: absolute;
    inset: 0;
    background:
      linear-gradient(135deg, var(--bg-purple) 0%, var(--bg-magenta) 38%, var(--bg-crimson) 70%, var(--bg-red) 100%);
  }
  .backdrop::after {
    content: "";
    position: absolute;
    inset: 0;
    background: radial-gradient(ellipse at 50% 35%, rgba(255,255,255,0.10), rgba(0,0,0,0) 60%);
  }
  .headline {
    position: absolute;
    left: 0;
    right: 0;
    text-align: center;
    font-family: "Righteous", sans-serif;
    text-transform: uppercase;
    text-shadow: 0 4px 6px rgba(80, 0, 40, 0.45);
  }
  .headline-intro {
    top: 92px;
    font-size: 33px;
    letter-spacing: 3px;
    color: var(--headline-pink);
  }
  .headline-main {
    top: 140px;
    font-size: 96px;
    line-height: 1;
    letter-spacing: 6px;
    background: linear-gradient(90deg, var(--headline-pink), var(--headline-rose));
    -webkit-background-clip: text;
    background-clip: text;
    color: transparent;
    text-shadow: none;
    filter: drop-shadow(0 5px 5px rgba(80, 0, 40, 0.5));
  }
  .headline-year {
    top: 248px;
    font-size: 104px;
    line-height: 1;
    letter-spacing: 4px;
    color: var(--year-pink);
  }
  .message {
    position: absolute;
    top: 426px;
    left: 0;
    right: 0;
    text-align: center;
    font-family: "Roboto", Arial, sans-serif;
    font-size: 26px;
    line-height: 34px;
    color: var(--body-pink);
  }
  .brand-panel {
    position: absolute;
    left: 384px;
    top: 600px;
    width: 434px;
    height: 310px;
    background: var(--card-white);
    border-radius: 14px 14px 0 0;
  }
  .brand-name {
    position: absolute;
    top: 122px;
    left: 0;
    right: 0;
    display: flex;
    align-items: center;
    justify-content: center;
    gap: 12px;
    font-family: "Roboto", Arial, sans-serif;
    font-weight: 700;
    font-size: 38px;
    letter-spacing: 1px;
    text-transform: uppercase;
    color: var(--brand-red);
  }
  .brand-dot {
    width: 18px;
    height: 18px;
    border-radius: 50%;
    background: var(--brand-red);
  }
  .brand-url {
    position: absolute;
    top: 237px;
    left: 0;
    right: 0;
    text-align: center;
    font-family: "Roboto", Arial, sans-serif;
    font-weight: 700;
    font-size: 24px;
    color: var(--ink);
  }
</style>
</head>
<body>
  <main class="greeting-card">
    <div class="backdrop" role="img" aria-label="Faceted geometric backdrop in purple, magenta and red tones with scattered snowflakes"></div>

    <p class="headline headline-intro">Merry Christmas &amp;</p>
    <h1 class="headline headline-main">Happy New Year!</h1>
    <p class="headline headline-year">2015</p>

    <p class="message">yout text goes here lorem ipsum dolor<br>consecterur dolor sit amet</p>

    <section class="brand-panel">
      <div class="brand-name"><span class="brand-dot"></span><span>Tovalix Tools</span></div>
      <p class="brand-url">www.tovalix.com.sg</p>
    </section>
  </main>
</body>
</html>
```